Design a helpdesk ticketing platform *

We are launching a helpdesk ticketing platform. Very much like quellbox.com, merrylark.com, pivolta.com, brisktray.com etc. We have a full mid-fidelity prototype built and we want someone to build the full fidelity of the product.

You can view the full mid-fidelity prototype here: https://lnk.vexora.net/Qa8Lpw

The best way moving forward is to just design the following 4 pages

- Main Dashboard https://lnk.vexora.net/81hRtd
- All tickets https://lnk.vexora.net/jwNoEb
- Viewing a ticket https://lnk.vexora.net/Ys4VmK
- Contacts https://lnk.vexora.net/pHeXuo

Target Market(s)

Small business owners

Industry/Entity Type

Saas

Number of Pages Required

4 page

Font styles to use
Serif
Sans Serif

Colors

Designer to choose colors to be used in the design.

Requirements
Must have
• Must follow the prototype exactly. We are not looking for any UX changes. We want the designe xactly as the prototype is. We are only looking for design ideas.
Should not have
• modern, clean. We'd love to see the primary color as yellow, purple, orange, green or blue. You choose which one you think looks best and go with that.

```html
<!DOCTYPE html>
<html lang="en">
<head>
<meta charset="utf-8">
<title>deskharbor – All Tickets</title>
<link rel="stylesheet" href="https://fonts.googleapis.com/css2?family=Montserrat:wght@400;500;600;700&display=swap">
<style>
:root{
  --side-top:#1b86aa;
  --side-bottom:#174a8a;
  --side-active:rgba(10,50,90,.35);
  --side-text:#ffffff;
  --accent:#1a93c0;
  --btn-a:#ef8a1e;
  --btn-b:#e5c21a;
  --ink:#1f2a33;
  --muted:#5b6670;
  --line:#d9dde1;
  --band:#f1f2f4;
  --danger:#d0342c;
  --white:#ffffff;
}
*{box-sizing:border-box;margin:0;padding:0}
html,body{width:1200px;height:824px;overflow:hidden;background:var(--white);font-family:"Montserrat",sans-serif;color:var(--ink)}
.app{position:relative;width:1200px;height:824px}

.sidebar{position:absolute;left:0;top:0;width:244px;height:824px;background:linear-gradient(180deg,var(--side-top),var(--side-bottom));color:var(--side-text)}
.brand{position:absolute;left:21px;top:20px;font-size:22px;font-weight:500;letter-spacing:.2px}
.menu-toggle{position:absolute;left:203px;top:27px;width:22px;height:16px}
.new-ticket{position:absolute;left:20px;top:63px;width:204px;height:39px;background:linear-gradient(90deg,var(--btn-a),var(--btn-b));color:#fff;font-size:12px;font-weight:600;display:flex;align-items:center;justify-content:center;gap:6px}
.side-rule{position:absolute;left:0;top:117px;width:244px;height:1px;background:rgba(255,255,255,.18)}
.nav-item{position:absolute;left:20px;display:flex;align-items:center;gap:10px;font-size:13.5px;font-weight:500}
.nav-item svg{width:18px;height:18px}
.nav-item.bold{font-weight:700}
.caret{position:absolute;left:216px;width:10px;height:10px}
.sub-active{position:absolute;left:0;top:241px;width:244px;height:40px;background:var(--side-active)}
.sub-item{position:absolute;left:52px;font-size:13px;font-weight:500}
.sub-rule{position:absolute;left:52px;top:408px;width:174px;height:1px;background:rgba(255,255,255,.35)}

.topbar{position:absolute;left:244px;top:0;width:956px;height:69px;border-bottom:1px solid var(--line)}
.crumb{position:absolute;left:19px;top:24px;font-size:18px;font-weight:400}
.crumb span{color:var(--accent)}
.search{position:absolute;left:637px;top:19px;width:204px;height:33px;border:1px solid #c9ced3;display:flex;align-items:center;gap:8px;padding-left:11px;font-size:11px;color:var(--muted)}
.me{position:absolute;left:858px;top:18px;width:34px;height:34px;border-radius:50%;background:var(--accent);color:#fff;font-size:14px;display:flex;align-items:center;justify-content:center}
.more{position:absolute;left:910px;top:32px;display:flex;gap:4px}
.more i{width:5px;height:5px;border-radius:50%;background:#9aa3ab;display:block}

.filters{position:absolute;left:244px;top:69px;width:262px;height:755px;border-right:1px solid var(--line)}
.filters-bar{height:49px;border-bottom:1px solid var(--line);position:relative}
.filters-title{position:absolute;left:5px;top:16px;display:flex;align-items:center;gap:8px;font-size:14px}
.discard{position:absolute;left:119px;top:19px;font-size:10.5px;text-decoration:underline}
.save-filter{position:absolute;left:167px;top:9px;width:95px;height:40px;border:1px solid var(--line);border-bottom:none;font-size:10.5px;display:flex;align-items:center;justify-content:center}
.field-label{position:absolute;left:17px;font-size:12px;font-weight:600}
.select{position:absolute;left:17px;width:234px;height:34px;border:1px solid #c9ced3;font-size:11.5px;display:flex;align-items:center;padding-left:9px}
.select .chev{position:absolute;right:10px;top:13px;width:10px;height:7px}
.tagbox{position:absolute;left:17px;width:234px;border:1px solid #c9ced3;padding:6px;display:flex;flex-wrap:wrap;gap:5px 5px}
.chip{border:1px solid #c9ced3;font-size:10.5px;height:21px;padding:0 5px 0 7px;display:flex;align-items:center;gap:6px}
.chip svg{width:7px;height:7px}

.tickets{position:absolute;left:506px;top:69px;width:694px;height:755px}
.table-bar{height:49px;position:relative}
.check{width:14px;height:14px;border:1px solid #c9ced3;border-radius:2px;background:#fff;position:absolute}
.select-all{position:absolute;left:35px;top:20px;font-size:10px}
.pager{position:absolute;left:589px;top:18px;font-size:10.5px;display:flex;align-items:center;gap:10px}
.thead{position:absolute;left:0;top:50px;width:694px;height:43px;background:var(--band);font-size:11.5px;font-weight:600}
.th,.td{position:absolute;white-space:nowrap}
.th{top:16px}
.row{position:absolute;left:0;width:694px;height:55px;border-bottom:1px solid var(--line);font-size:12px}
.row .td{top:20px}
.avatar{position:absolute;left:36px;top:13px;width:28px;height:28px;border-radius:50%;background:var(--accent);color:#fff;font-size:10.5px;display:flex;align-items:center;justify-content:center}
.state{color:var(--danger)}
.dd{display:flex;align-items:center;gap:8px}
.dd svg{width:10px;height:7px}
.acts{position:absolute;left:314px;top:22px;display:flex;gap:12px}
</style>
</head>
<body>
<div class="app">

  <aside class="sidebar">
    <div class="brand">deskharbor</div>
    <svg class="menu-toggle" viewBox="0 0 22 16"><path d="M0 1h22M0 8h22M0 15h22" stroke="#fff" stroke-width="2"/></svg>
    <div class="new-ticket">New Ticket <svg width="11" height="11" viewBox="0 0 11 11"><path d="M5.5 0v11M0 5.5h11" stroke="#fff" stroke-width="2"/></svg></div>
    <div class="side-rule"></div>

    <div class="nav-item" style="top:152px"><svg viewBox="0 0 18 18" fill="none" stroke="#fff" stroke-width="1.4"><circle cx="9" cy="9" r="7.5"/><path d="M9 9l3-3"/><circle cx="9" cy="9" r="1"/></svg>Dashboard</div>
    <div class="nav-item bold" style="top:204px"><svg viewBox="0 0 18 18"><path d="M2 11l7-7 5 1 1 5-7 7z" fill="#fff"/><circle cx="12" cy="6" r="1.3" fill="#1b7fa6"/></svg>Tickets</div>
    <svg class="caret" style="top:210px" viewBox="0 0 10 10"><path d="M1 7l4-4 4 4" stroke="#fff" stroke-width="1.4" fill="none"/></svg>

    <div class="sub-active"></div>
    <div class="sub-item" style="top:253px">All Tickets</div>
    <div class="sub-item" style="top:292px">My Tickets</div>
    <div class="sub-item" style="top:330px">Open Tickets</div>
    <div class="sub-item" style="top:368px">Unassigned Tickets</div>
    <div class="sub-rule"></div>
    <div class="sub-item" style="top:431px">Spam</div>
    <div class="sub-item" style="top:466px">Trash</div>

    <div class="nav-item" style="top:516px"><svg viewBox="0 0 18 18" fill="none" stroke="#fff" stroke-width="1.3"><rect x="1" y="3" width="16" height="12"/><circle cx="6" cy="8" r="2"/><path d="M3 13c0-2 6-2 6 0M11 7h4M11 10h4"/></svg>Contacts</div>
    <div class="nav-item" style="top:567px"><svg viewBox="0 0 18 18" fill="none" stroke="#fff" stroke-width="1.3"><circle cx="9" cy="9" r="2.6"/><path d="M9 1.5v2.3M9 14.2v2.3M1.5 9h2.3M14.2 9h2.3M3.7 3.7l1.6 1.6M12.7 12.7l1.6 1.6M3.7 14.3l1.6-1.6M12.7 5.3l1.6-1.6"/><circle cx="9" cy="9" r="5.4"/></svg>Admin Settings</div>
    <svg class="caret" style="top:579px" viewBox="0 0 10 10"><path d="M1 3l4 4 4-4" stroke="#fff" stroke-width="1.4" fill="none"/></svg>
    <div class="nav-item" style="top:618px"><svg viewBox="0 0 18 18" fill="none" stroke="#fff" stroke-width="1.3"><rect x="1" y="4" width="16" height="11"/><path d="M1 7.5h16"/></svg>Account &amp; Billing</div>
  </aside>

  <header class="topbar">
    <div class="crumb">Tickets / <span>All Tickets</span></div>
    <div class="search"><svg width="14" height="14" viewBox="0 0 14 14" fill="none" stroke="#5b6670" stroke-width="1.3"><circle cx="8" cy="6" r="4.5"/><path d="M4.8 9.2L1 13"/></svg>Search</div>
    <div class="me">AK</div>
    <div class="more"><i></i><i></i><i></i></div>
  </header>

  <section class="filters">
    <div class="filters-bar">
      <div class="filters-title">
        <svg width="6" height="9" viewBox="0 0 6 9"><path d="M5 1L1.5 4.5 5 8" stroke="#5b6670" fill="none"/></svg>
        <svg width="18" height="16" viewBox="0 0 18 16" fill="none" stroke="#1a6fa8" stroke-width="1.4"><path d="M0 2.5h18M0 8h18M0 13.5h18"/><circle cx="5" cy="2.5" r="2" fill="#fff"/><circle cx="12" cy="8" r="2" fill="#fff"/><circle cx="6" cy="13.5" r="2" fill="#fff"/></svg>
        Filters
      </div>
      <div class="discard">Discard</div>
      <div class="save-filter">Save filter as</div>
    </div>

    <div class="field-label" style="top:65px">Agents</div>
    <div class="tagbox" style="top:87px;height:59px">
      <div class="chip">Elliot <svg viewBox="0 0 7 7"><path d="M0 0l7 7M7 0L0 7" stroke="#1f2a33" stroke-width="1.3"/></svg></div>
      <div class="chip">Ravi <svg viewBox="0 0 7 7"><path d="M0 0l7 7M7 0L0 7" stroke="#1f2a33" stroke-width="1.3"/></svg></div>
      <div class="chip">Dana <svg viewBox="0 0 7 7"><path d="M0 0l7 7M7 0L0 7" stroke="#1f2a33" stroke-width="1.3"/></svg></div>
      <div class="chip">Priya <svg viewBox="0 0 7 7"><path d="M0 0l7 7M7 0L0 7" stroke="#1f2a33" stroke-width="1.3"/></svg></div>
      <div class="chip">Jonah <svg viewBox="0 0 7 7"><path d="M0 0l7 7M7 0L0 7" stroke="#1f2a33" stroke-width="1.3"/></svg></div>
    </div>

    <div class="field-label" style="top:161px">Groups</div>
    <div class="select" style="top:184px">Any<svg class="chev" viewBox="0 0 10 7"><path d="M1 1l4 4 4-4" stroke="#1f2a33" stroke-width="1.3" fill="none"/></svg></div>
    <div class="field-label" style="top:234px">Created</div>
    <div class="select" style="top:258px">Any<svg class="chev" viewBox="0 0 10 7"><path d="M1 1l4 4 4-4" stroke="#1f2a33" stroke-width="1.3" fill="none"/></svg></div>
    <div class="field-label" style="top:307px">Status</div>
    <div class="select" style="top:330px">Any<svg class="chev" viewBox="0 0 10 7"><path d="M1 1l4 4 4-4" stroke="#1f2a33" stroke-width="1.3" fill="none"/></svg></div>
    <div class="field-label" style="top:382px">Piority</div>
    <div class="select" style="top:405px;padding-left:7px;gap:5px">
      <div class="chip">Low <svg viewBox="0 0 7 7"><path d="M0 0l7 7M7 0L0 7" stroke="#1f2a33" stroke-width="1.3"/></svg></div>
      <div class="chip">High <svg viewBox="0 0 7 7"><path d="M0 0l7 7M7 0L0 7" stroke="#1f2a33" stroke-width="1.3"/></svg></div>
      <div class="chip">Urgent <svg viewBox="0 0 7 7"><path d="M0 0l7 7M7 0L0 7" stroke="#1f2a33" stroke-width="1.3"/></svg></div>
      <svg class="chev" viewBox="0 0 10 7"><path d="M1 1l4 4 4-4" stroke="#1f2a33" stroke-width="1.3" fill="none"/></svg>
    </div>
    <div class="field-label" style="top:454px">Source</div>
    <div class="select" style="top:477px">Any<svg class="chev" viewBox="0 0 10 7"><path d="M1 1l4 4 4-4" stroke="#1f2a33" stroke-width="1.3" fill="none"/></svg></div>
    <div class="field-label" style="top:527px">Tags</div>
    <div class="select" style="top:551px">Any<svg class="chev" viewBox="0 0 10 7"><path d="M1 1l4 4 4-4" stroke="#1f2a33" stroke-width="1.3" fill="none"/></svg></div>
    <div class="field-label" style="top:601px">Companies</div>
    <div class="select" style="top:624px">Any<svg class="chev" viewBox="0 0 10 7"><path d="M1 1l4 4 4-4" stroke="#1f2a33" stroke-width="1.3" fill="none"/></svg></div>
    <div class="field-label" style="top:674px">Contacts</div>
    <div class="select" style="top:697px">Any<svg class="chev" viewBox="0 0 10 7"><path d="M1 1l4 4 4-4" stroke="#1f2a33" stroke-width="1.3" fill="none"/></svg></div>
  </section>

  <section class="tickets">
    <div class="table-bar">
      <span class="check" style="left:10px;top:18px"></span>
      <div class="select-all">Select all</div>
      <div class="pager">1-25 of 10
        <svg width="8" height="13" viewBox="0 0 8 13"><path d="M7 1L2 6.5 7 12" stroke="#1f2a33" stroke-width="1.5" fill="none"/></svg>
        <svg width="8" height="13" viewBox="0 0 8 13"><path d="M1 1l5 5.5L1 12" stroke="#1f2a33" stroke-width="1.5" fill="none"/></svg>
      </div>
    </div>

    <div class="thead">
      <div class="th" style="left:34px">Contact</div>
      <div class="th" style="left:192px">Subject</div>
      <div class="th" style="left:362px">State</div>
      <div class="th" style="left:450px">Group</div>
      <div class="th" style="left:530px">Agent</div>
      <div class="th" style="left:628px">Priority</div>
    </div>

    <div class="row" style="top:93px">
      <span class="check" style="left:10px;top:20px"></span>
      <div class="avatar">NW</div>
      <div class="td" style="left:70px">Nora Whitfield</div>
      <div class="td" style="left:192px">I can’t reset... (#10)</div>
      <div class="acts"><svg width="12" height="9" viewBox="0 0 12 9"><path d="M0 4.5C3-1 9-1 12 4.5 9 10 3 10 0 4.5z" fill="#1a93c0"/><circle cx="6" cy="4.5" r="1.6" fill="#fff"/></svg><svg width="9" height="9" viewBox="0 0 9 9"><path d="M1 8l1-3 4-4 2 2-4 4z" fill="#1a93c0"/></svg></div>
      <div class="td state" style="left:363px">Past Due</div>
      <div class="td dd" style="left:450px">Sales <svg viewBox="0 0 10 7"><path d="M1 1l4 4 4-4" stroke="#1f2a33" stroke-width="1.3" fill="none"/></svg></div>
      <div class="td dd" style="left:530px">Marcus <svg viewBox="0 0 10 7"><path d="M1 1l4 4 4-4" stroke="#1f2a33" stroke-width="1.3" fill="none"/></svg></div>
      <div class="td dd" style="left:631px">Low <svg viewBox="0 0 10 7"><path d="M1 1l4 4 4-4" stroke="#1f2a33" stroke-width="1.3" fill="none"/></svg></div>
    </div>

    <div class="row" style="top:148px">
      <span class="check" style="left:10px;top:20px"></span>
      <div class="avatar">PH</div>
      <div class="td" style="left:70px">Priya Halden</div>
      <div class="td" style="left:192px">Forgot to CC (#15</div>
      <div class="acts"><svg width="12" height="9" viewBox="0 0 12 9"><path d="M0 4.5C3-1 9-1 12 4.5 9 10 3 10 0 4.5z" fill="#1a93c0"/><circle cx="6" cy="4.5" r="1.6" fill="#fff"/></svg><svg width="9" height="9" viewBox="0 0 9 9"><path d="M1 8l1-3 4-4 2 2-4 4z" fill="#1a93c0"/></svg></div>
      <div class="td state" style="left:363px">Past Due</div>
      <div class="td dd" style="left:450px">Sales <svg viewBox="0 0 10 7"><path d="M1 1l4 4 4-4" stroke="#1f2a33" stroke-width="1.3" fill="none"/></svg></div>
      <div class="td dd" style="left:530px">Marcus <svg viewBox="0 0 10 7"><path d="M1 1l4 4 4-4" stroke="#1f2a33" stroke-width="1.3" fill="none"/></svg></div>
      <div class="td dd" style="left:631px">Low <svg viewBox="0 0 10 7"><path d="M1 1l4 4 4-4" stroke="#1f2a33" stroke-width="1.3" fill="none"/></svg></div>
    </div>

    <div class="row" style="top:203px">
      <span class="check" style="left:10px;top:20px"></span>
      <div class="avatar">TG</div>
      <div class="td" style="left:70px">Tomas Greer</div>
      <div class="td" style="left:192px">Forgot to CC (#15</div>
      <div class="acts"><svg width="12" height="9" viewBox="0 0 12 9"><path d="M0 4.5C3-1 9-1 12 4.5 9 10 3 10 0 4.5z" fill="#1a93c0"/><circle cx="6" cy="4.5" r="1.6" fill="#fff"/></svg><svg width="9" height="9" viewBox="0 0 9 9"><path d="M1 8l1-3 4-4 2 2-4 4z" fill="#1a93c0"/></svg></div>
      <div class="td state" style="left:363px">Past Due</div>
      <div class="td dd" style="left:450px">Sales <svg viewBox="0 0 10 7"><path d="M1 1l4 4 4-4" stroke="#1f2a33" stroke-width="1.3" fill="none"/></svg></div>
      <div class="td dd" style="left:530px">Marcus <svg viewBox="0 0 10 7"><path d="M1 1l4 4 4-4" stroke="#1f2a33" stroke-width="1.3" fill="none"/></svg></div>
      <div class="td dd" style="left:631px">Low <svg viewBox="0 0 10 7"><path d="M1 1l4 4 4-4" stroke="#1f2a33" stroke-width="1.3" fill="none"/></svg></div>
    </div>
  </section>

</div>
</body>
</html>
```